Black Friday Sale Social Media Graphics

Focusing on Black Friday Graphics for each of the pics attached.  So need the product pics turned into  social media graphics (square size). For the color scheme of the graphics, they should all be complementary to the product colors.
You can add any of the stock photography attached but none are required. I mainly need BOLD text that says:
Black Friday Sale
Up to $15 Off
If you wanted to add smaller text, these headlines can work:
1.	Burn Belly Fat Fast!
2.	Double Your Weight Loss With Our Supplements!
3.	Lose Weight Naturally: Ditch the Prescription Pills & Needles!
4.	Tired of Stubborn Belly Fat? Discover What Works!
5.	Melt Away Belly Fat Faster with Our Supplements!
6.	Struggling to Lose Weight? Discover the Ultimate Solution!
7.	Ready to Burn Fat Faster?

Target Market(s)
women trying to lose weight
Industry/Entity Type
health and wellness
Requirements
Must have
- the product pics attached

Nice to have
- Bold text that says: Black Friday Sale

```html
<!DOCTYPE html>
<html lang="en">
<head>
<meta charset="utf-8">
<title>Black Friday Sale – Social Media Graphics</title>
<link rel="stylesheet" href="https://fonts.googleapis.com/css2?family=Montserrat:wght@900&family=Poppins:wght@400;500;600;800&family=Kaushan+Script&display=swap">
<style>
  :root{
    --board:#1b2932;
    --navy:#1a1b44;
    --teal:#2f8c88;
    --teal-deep:#1f5f66;
    --mint:#3fc6b5;
    --lilac:#a78be0;
    --pink:#ff5ed8;
    --magenta:#d65fd7;
    --red:#ff1a2e;
    --white:#ffffff;
    --ink:#1b2040;
    --grey-badge:rgba(120,110,115,.85);
  }
  *{box-sizing:border-box;margin:0;padding:0}
  html,body{width:860px;height:1200px;overflow:hidden;background:var(--board)}
  .board{position:relative;width:860px;height:1200px;background:var(--board)}

  .board-title{
    position:absolute;left:0;right:0;top:6px;text-align:center;
    font-family:"Poppins",sans-serif;font-weight:400;font-size:70px;line-height:1;letter-spacing:-.5px;
    background:linear-gradient(90deg,var(--mint) 0%,var(--mint) 38%,var(--lilac) 55%,var(--magenta) 70%,#d970e0 100%);
    -webkit-background-clip:text;background-clip:text;color:transparent;
  }
  .board-subtitle{
    position:absolute;left:0;right:0;top:62px;text-align:center;
    font-family:"Kaushan Script",cursive;font-size:32px;color:var(--white);line-height:1;
  }

  .post{position:absolute;width:300px;height:300px;overflow:hidden}
  .post svg.shape{position:absolute;inset:0;width:300px;height:300px}

  .headline{
    position:absolute;left:16px;top:22px;z-index:2;
    font-family:"Montserrat",sans-serif;font-weight:900;font-size:48px;line-height:46px;letter-spacing:-2.4px;
    color:var(--white);text-shadow:2px 3px 3px rgba(10,15,40,.45);
  }
  .headline span{display:block}
  .headline--dark{
    background:linear-gradient(160deg,var(--ink) 0%,var(--teal) 45%,var(--ink) 100%);
    -webkit-background-clip:text;background-clip:text;color:transparent;text-shadow:none;
  }

  .badge{
    position:absolute;z-index:3;width:90px;height:90px;border-radius:50%;
    display:flex;flex-direction:column;align-items:center;justify-content:center;
    font-family:"Poppins",sans-serif;color:var(--white);text-align:center;
  }
  .badge .upto,.badge .off{font-size:13px;font-weight:500;line-height:1.15}
  .badge .amount{font-size:31px;font-weight:800;line-height:1.05;letter-spacing:-.5px}

  .photo{
    position:absolute;z-index:1;border-radius:6px;
    background:linear-gradient(180deg,rgba(255,255,255,.95) 0%,rgba(236,236,240,.92) 70%,rgba(210,210,220,.85) 100%);
  }

  /* post 1 */
  .post--1{left:103px;top:136px;
    background:
      radial-gradient(circle at 100% 0%,var(--red) 0%,rgba(255,26,46,0) 30%),
      linear-gradient(200deg,var(--pink) 0%,#e06fe0 28%,var(--teal) 55%,var(--teal-deep) 75%,var(--navy) 100%);}
  .post--1 .badge{left:197px;top:69px;background:rgba(170,60,160,.55)}
  .post--1 .photo{left:33px;top:181px;width:229px;height:111px}

  /* post 2 */
  .post--2{left:434px;top:136px;
    background:linear-gradient(200deg,#e8a0b8 0%,#5fa59e 30%,var(--teal) 55%,var(--teal-deep) 75%,var(--navy) 100%);}
  .post--2 .badge{left:25px;top:181px;background:var(--grey-badge)}
  .post--2 .photo{left:151px;top:123px;width:138px;height:169px}

  /* post 3 */
  .post--3{left:103px;top:463px;
    background:linear-gradient(200deg,var(--teal-deep) 0%,#2a6d72 40%,var(--teal) 100%);}
  .post--3 .badge{left:36px;top:189px;background:var(--grey-badge)}
  .post--3 .photo--bottle{left:164px;top:153px;width:70px;height:135px}
  .post--3 .photo--tube{left:234px;top:80px;width:50px;height:208px}

  /* post 4 */
  .post--4{left:434px;top:461px;
    background:linear-gradient(155deg,var(--teal-deep) 0%,var(--teal) 35%,#8e8ed8 65%,#e48ae6 85%,var(--pink) 100%);}
  .post--4 .badge{left:197px;top:60px;background:rgba(80,90,135,.7)}
  .post--4 .photo{left:42px;top:167px;width:217px;height:124px}

  /* post 5 */
  .post--5{left:103px;top:791px;
    background:linear-gradient(160deg,var(--navy) 0%,var(--teal-deep) 25%,var(--teal) 50%,#9a92d8 78%,#e07ae4 100%);}
  .post--5 .badge{left:30px;top:184px;background:rgba(70,100,125,.6)}
  .post--5 .photo--person{left:165px;top:58px;width:135px;height:180px;border-radius:0;
    background:linear-gradient(180deg,rgba(255,255,255,.45) 0%,rgba(245,245,248,.8) 60%,rgba(255,255,255,.9) 100%);}
  .post--5 .photo--row{left:130px;top:238px;width:170px;height:62px;border-radius:0}

  /* post 6 */
  .post--6{left:434px;top:791px;
    background:linear-gradient(150deg,var(--navy) 0%,#5a3aa0 30%,#c25ad8 55%,var(--pink) 78%,var(--red) 100%);}
  .post--6 .badge{left:195px;top:51px;background:var(--grey-badge)}
  .post--6 .photo{left:42px;top:167px;width:215px;height:130px}
</style>
</head>
<body>
<main class="board">
  <h1 class="board-title">Black Friday Sale</h1>
  <p class="board-subtitle">Social Media Graphics</p>

  <section class="post post--1">
    <h2 class="headline"><span>BLACK</span><span>FRIDAY</span><span>SALE</span></h2>
    <div class="badge"><span class="upto">Upto</span><span class="amount">$15</span><span class="off">OFF</span></div>
    <div class="photo" role="img" aria-label="Product photo: four white supplement bottles in a row"></div>
  </section>

  <section class="post post--2">
    <svg class="shape" viewBox="0 0 300 300" aria-hidden="true"><path d="M0 0H212C190 90 150 170 70 235L0 290Z" fill="#ffffff"/></svg>
    <h2 class="headline headline--dark"><span>BLACK</span><span>FRIDAY</span><span>SALE</span></h2>
    <div class="badge"><span class="upto">Upto</span><span class="amount">$15</span><span class="off">OFF</span></div>
    <div class="photo" role="img" aria-label="Product photo: two cream tubes and a supplement bottle"></div>
  </section>

  <section class="post post--3">
    <svg class="shape" viewBox="0 0 300 300" aria-hidden="true"><path d="M0 0H196C215 40 200 120 140 180C90 225 40 260 0 285Z" fill="#ffffff"/></svg>
    <h2 class="headline headline--dark"><span>BLACK</span><span>FRIDAY</span><span>SALE</span></h2>
    <div class="badge"><span class="upto">Upto</span><span class="amount">$15</span><span class="off">OFF</span></div>
    <div class="photo photo--bottle" role="img" aria-label="Product photo: a supplement bottle"></div>
    <div class="photo photo--tube" role="img" aria-label="Product photo: a tall cream tube"></div>
  </section>

  <section class="post post--4">
    <h2 class="headline"><span>BLACK</span><span>FRIDAY</span><span>SALE</span></h2>
    <div class="badge"><span class="upto">Upto</span><span class="amount">$15</span><span class="off">OFF</span></div>
    <div class="photo" role="img" aria-label="Product photo: four supplement bottles grouped together"></div>
  </section>

  <section class="post post--5">
    <h2 class="headline"><span>BLACK</span><span>FRIDAY</span><span>SALE</span></h2>
    <div class="photo photo--person" role="img" aria-label="Photo: smiling woman standing behind the products"></div>
    <div class="photo photo--row" role="img" aria-label="Product photo: a row of bottles and tubes"></div>
    <div class="badge"><span class="upto">Upto</span><span class="amount">$15</span><span class="off">OFF</span></div>
  </section>

  <section class="post post--6">
    <svg class="shape" viewBox="0 0 300 300" aria-hidden="true"><path d="M180 0H300V262C250 210 205 130 180 0Z" fill="#ffffff"/></svg>
    <h2 class="headline"><span>BLACK</span><span>FRIDAY</span><span>SALE</span></h2>
    <div class="badge"><span class="upto">Upto</span><span class="amount">$15</span><span class="off">OFF</span></div>
    <div class="photo" role="img" aria-label="Product photo: three supplement bottles side by side"></div>
  </section>
</main>
</body>
</html>
```